Bifold brochure design for leadership academy

Please see below. This is a bifold brochure for a leadership academy. (www.vtq.institute). Look and feel must be colours, shapes, abstract designs, graphics, pictures. Make this professional, yet casual and bold.

Feel free to design just the front and back cover, then I'll give feedback on whether or not you're in the right direction.

COVER
- Title: “The Ultimate Gap Year Program”
- “Northbrook Mentorship Institute” logo somewhere
- Subtitles (with images, icons, and/or shapes): “Self-discovery” “Skills development” “Real-world Impact”

PAGE 2 (Inside Fold)
- Title: "The Program"
- Section 2a: Section title: "How it works”
- Image: See website, image under "four phases of the program". Please adapt and make it look better
- Text: NMI is a structured, 8-month ‘gap year’ program for 18-25 year olds who want more than just a year off – they want a year ahead. Our aim is to develop high-potential young leaders with strong values, clear purpose, high-impact skills, and a track record of real-world accomplishments that are second-to-none. We do this through four-phases.
- Section 2b: Section title: “Dates & Timing”
- Image: See image on website under 'dates and timing'. Make sure both dates show up on the brochure (September and January program).
- Text: There are two programs per year: one that starts in September, the other in January. The first four months of the program are based in Toronto at the NMI headquarters. The curriculum we work through is highly engaging and personalized, focusing directly on students’ goals. After that, students are out in the world, achieving the remaining components of the program (e.g. internship, volunteer abroad).

PAGE 3 (Outside Fold)
- Page Title: "The Students"
- Section 3a: Section title: “Who’s it for”
- Subtitle1: “High school graduates”
 Image/icon of a high school grad
 Text1: 90% of high school grads aren't sure why they’re going to university or what they want to study.
 Text2: NMI helps students discover what they truly want to do in life, and make enormous progress towards these goals.

- Subtitle2: “Post-secondary students”
 Image/icon of a university / college student
 Text1: 28% of students switch or drop out of their program because it wasn’t for them or they didn’t like it.
 Text2: Don't keep moving around or risk switching careers down the road – find out what sparks your passion with NMI.

- Subtitle3: “Post-secondary graduates”
 Image/icon of a university/ college grad
 Text1: 50% of graduates are unemployed or underemployed, 60% are in debt.
 Text2: NMI will help you get your dream job – our students won’t settle for anything less.

- Section 3b: Section title: “How to apply”
 Text1: We select high-potential young leaders with a desire to improve themselves and impact the world.
 Text2: We won’t ask you for your grades – we care more about your values and potential.
 Text3: Visit www.vtq.institute to apply now

BACK COVER
- Page Title: “Get in Touch”
- Website: www.vtq.institute
- Facebook page: facebook.com/vtq.institute
- Twitter handle: @vtq_institute
- Email: brent@vtq.institute

Project Deadline Extended Reason: Made a mistake initially only giving designers 2 days to submit. This allows for more high quality designs. Thank you. Added Wednesday, March 18, 2015

18-25 year olds, parents, teachers

Leadership

• Beautiful design - sleek and bold, yet colourful and casual. Keep the colours similar to our website (www.vtq.institute). See examples of other brochures.
• http://img.plorvex.net/jpg/00/11/22/33/240_F_11223344_aBcDeFgHiJkLmNoPqRsTuVwXyZ0123.jpg
• http://quelmarsite.com/wp-content/uploads/2014/11/Sample-Bi-fold-Brochure.jpg
• http://www.vantrello.com/media/k2/galleries/5/001-bi-fold-brochure-psd-mock-up-template.jpg
• http://img.plorvex.net/jpg/00/44/55/66/240_F_44556677_zYxWvUtSrQpOnMlKjIhGfEdCbA9876.jpg

```html
<!DOCTYPE html>
<html lang="en">
<head>
<meta charset="utf-8">
<title>Northbrook Mentorship Institute – Gap Year Program Brochure</title>
<link rel="stylesheet" href="https://fonts.googleapis.com/css2?family=Arimo:wght@400;700&display=swap">
<style>
  :root {
    --backdrop: #e4e4e4;
    --maroon: #5b1e29;
    --maroon-deep: #3f141d;
    --red: #b3202a;
    --cream: #f4efcf;
    --beige: #e9cfa6;
    --beige-deep: #d9b98c;
    --navy: #1d2f4d;
    --shirt-blue: #2d5d92;
    --brand-red: #b8262d;
    --ink: #1b1b1b;
    --white: #ffffff;
  }
  * { margin: 0; padding: 0; box-sizing: border-box; }
  html, body { width: 1200px; height: 900px; overflow: hidden; background: var(--backdrop); }
  body { font-family: "Arimo", Arial, sans-serif; position: relative; }

  .spread {
    position: absolute; left: 120px; top: 120px;
    width: 960px; height: 660px;
    box-shadow: 0 18px 40px rgba(0,0,0,.25);
    overflow: hidden;
  }
  .spread-art { position: absolute; inset: 0; width: 960px; height: 660px; }

  /* Back cover */
  .contact-title {
    position: absolute; left: 20px; top: 438px;
    color: var(--brand-red); font-weight: 700; font-size: 17px;
  }
  .contact-list { position: absolute; left: 20px; top: 470px; list-style: none; }
  .contact-item {
    display: flex; align-items: center; gap: 8px;
    height: 26px; font-size: 11px; color: var(--ink); white-space: nowrap;
  }
  .contact-icon { width: 18px; height: 18px; flex: none; }

  /* Front cover */
  .brand-lockup {
    position: absolute; right: 22px; top: 18px; width: 120px;
    color: var(--brand-red); font-weight: 700; text-align: left;
  }
  .brand-mark { font-size: 34px; line-height: 1; letter-spacing: 1px; }
  .brand-name { font-size: 7.5px; letter-spacing: 2.4px; line-height: 1.25; text-transform: uppercase; margin-top: 2px; }

  .cover-title {
    position: absolute; left: 430px; top: 205px;
    display: flex; align-items: flex-end;
    color: var(--white); font-weight: 400;
  }
  .cover-kicker { font-size: 14px; line-height: 1.25; text-align: right; margin-right: 4px; padding-bottom: 6px; }
  .cover-main { font-size: 46px; line-height: 1; }

  .pillar-list { position: absolute; left: 700px; top: 482px; list-style: none; }
  .pillar {
    display: flex; align-items: center; gap: 10px;
    height: 35px; font-size: 13px; color: var(--brand-red);
  }
  .pillar-hex { width: 26px; height: 26px; flex: none; }
</style>
</head>
<body>
<main class="spread">
  <svg class="spread-art" viewBox="0 0 960 660">
    <defs>
      <linearGradient id="portraitTone" x1="0" y1="0" x2="0" y2="1">
        <stop offset="0" stop-color="#1d2f4d"/>
        <stop offset=".45" stop-color="#2d5d92"/>
        <stop offset=".55" stop-color="#6b2330"/>
        <stop offset="1" stop-color="#8e1f2a"/>
      </linearGradient>
      <linearGradient id="beigePanel" x1="0" y1="0" x2="1" y2="1">
        <stop offset="0" stop-color="#f1dcb6"/>
        <stop offset="1" stop-color="#d9b98c"/>
      </linearGradient>
    </defs>

    <rect class="base-field" width="960" height="660" fill="var(--maroon)"/>
    <polygon class="left-band" points="0,0 130,0 250,150 300,300 300,450 0,140" fill="var(--maroon-deep)" opacity=".55"/>

    <polygon class="lower-red-field" points="80,660 300,450 360,420 400,660" fill="var(--red)"/>

    <g role="img" aria-label="Photo of a young man in glasses and a shirt, looking down while writing">
      <polygon points="230,0 720,0 740,390 470,620 500,660 330,660 300,450 250,150" fill="url(#portraitTone)"/>
    </g>
    <circle class="focus-ring" cx="525" cy="140" r="56" fill="none" stroke="var(--white)" stroke-width="2"/>

    <polygon class="top-left-wedge" points="130,0 300,0 250,150" fill="var(--cream)"/>
    <polygon class="contact-panel" points="0,140 300,450 80,660 0,660" fill="var(--cream)"/>
    <polygon class="logo-panel" points="700,0 960,0 960,40 840,160" fill="var(--cream)"/>

    <polygon class="pillar-edge" points="455,626 960,292 960,302 470,620" fill="var(--cream)"/>
    <polygon class="pillar-panel" points="470,620 960,302 960,660 500,660" fill="url(#beigePanel)"/>

    <line class="fold-line" x1="480" y1="0" x2="480" y2="660" stroke="#000" stroke-opacity=".12" stroke-width="1"/>
  </svg>

  <!-- Back cover -->
  <h2 class="contact-title">Get in Touch</h2>
  <ul class="contact-list">
    <li class="contact-item">
      <svg class="contact-icon" viewBox="0 0 18 18"><circle cx="9" cy="9" r="9" fill="var(--ink)"/></svg>
      circlepage.com/vtq.institute
    </li>
    <li class="contact-item">
      <svg class="contact-icon" viewBox="0 0 18 18"><circle cx="9" cy="9" r="9" fill="var(--ink)"/></svg>
      @vtq_institute
    </li>
    <li class="contact-item">
      <svg class="contact-icon" viewBox="0 0 18 18">
        <circle cx="9" cy="9" r="9" fill="var(--ink)"/>
        <circle cx="9" cy="9" r="5.5" fill="none" stroke="var(--white)" stroke-width="1"/>
        <ellipse cx="9" cy="9" rx="2.4" ry="5.5" fill="none" stroke="var(--white)" stroke-width="1"/>
        <line x1="3.5" y1="9" x2="14.5" y2="9" stroke="var(--white)" stroke-width="1"/>
      </svg>
      www.vtq.institute
    </li>
    <li class="contact-item">
      <svg class="contact-icon" viewBox="0 0 18 18">
        <circle cx="9" cy="9" r="9" fill="var(--ink)"/>
        <rect x="4.5" y="6" width="9" height="6.5" fill="var(--white)"/>
        <polyline points="4.5,6 9,10 13.5,6" fill="none" stroke="var(--ink)" stroke-width="1"/>
      </svg>
      brent@vtq.institute
    </li>
  </ul>

  <!-- Front cover -->
  <div class="brand-lockup">
    <div class="brand-mark">NMI</div>
    <div class="brand-name">Northbrook<br>Mentorship<br>Institute</div>
  </div>

  <h1 class="cover-title">
    <span class="cover-kicker">The Ultimate<br>Gap YeaR</span>
    <span class="cover-main">Program</span>
  </h1>

  <ul class="pillar-list">
    <li class="pillar">
      <svg class="pillar-hex" viewBox="0 0 26 26"><polygon points="13,1 24,7 24,19 13,25 2,19 2,7" fill="#d9553a"/></svg>
      Self-discovery
    </li>
    <li class="pillar">
      <svg class="pillar-hex" viewBox="0 0 26 26"><polygon points="13,1 24,7 24,19 13,25 2,19 2,7" fill="#5b63a8"/></svg>
      Skills Development
    </li>
    <li class="pillar">
      <svg class="pillar-hex" viewBox="0 0 26 26"><polygon points="13,1 24,7 24,19 13,25 2,19 2,7" fill="#e0683f"/></svg>
      Real-world Impact
    </li>
  </ul>
</main>
</body>
</html>
```